Stationary Design for Landscaping & Cleaning Business

Our landscaping and cleaning business need a stationary design, we would like separate designs for each business that match.
We want a simple yet bold design, using colours of our logos.
We are re designing our business so we need a more professional and modern look.
We don't want any extra words, just the basic contact details.
Name, address, phone number, email, abn and the usual customer details.
We would like to see examples for all stationary and both names.

Target Market(s)

No target market

Industry/Entity Type

Business

Font styles to use
Sans Serif

Colors
ffffff
000000

Requirements
Must have
• Business card, letterhead and envelope design.
Nice to have
• Lines and coloured areas
Should not have
• No extra pictures

```html
<!DOCTYPE html>
<html lang="en">
<head>
<meta charset="utf-8">
<title>Fernway Grounds – Stationery</title>
<link rel="stylesheet" href="https://fonts.googleapis.com/css2?family=Didact+Gothic&family=Mulish:wght@800&display=swap">
<style>
  :root {
    --board-top: #d4d4d4;
    --board-mid: #9a9a9a;
    --board-bottom: #585858;
    --panel: rgba(232, 232, 232, 0.9);
    --panel-edge: #3a3a3a;
    --paper: #ffffff;
    --ink: #111111;
    --leaf: #6bd200;
  }
  * { box-sizing: border-box; margin: 0; padding: 0; }
  html, body { width: 900px; height: 1200px; overflow: hidden; }
  body {
    position: relative;
    font-family: "Didact Gothic", "Century Gothic", sans-serif;
    color: var(--ink);
  }
  .backdrop {
    position: absolute; inset: 0;
    background:
      linear-gradient(135deg, rgba(255,255,255,0.10) 0%, rgba(255,255,255,0) 40%),
      linear-gradient(180deg, var(--board-top) 0%, var(--board-mid) 45%, var(--board-bottom) 100%);
  }
  .section-label {
    position: absolute;
    font-family: "Mulish", "Century Gothic", sans-serif;
    font-weight: 800;
    font-size: 26px;
    line-height: 1;
    color: #000;
  }
  .panel {
    position: absolute;
    background: var(--panel);
    border: 1px solid var(--panel-edge);
    border-radius: 18px;
  }
  .wordmark {
    position: absolute;
    font-family: "Didact Gothic", "Century Gothic", sans-serif;
    color: var(--ink);
    white-space: nowrap;
    line-height: 1;
    letter-spacing: -0.03em;
  }
  .band { position: absolute; background: var(--leaf); }
  .contact {
    position: absolute;
    white-space: nowrap;
    line-height: 1.2;
    color: var(--ink);
  }
  .contact .sep { display: inline-block; width: 1px; height: 0.95em; background: var(--ink); margin: 0 0.5em; vertical-align: -0.1em; }

  /* letterhead */
  .letterhead { position: absolute; left: 0; top: 0; }
  .letterhead .wordmark { left: 0; width: 757px; text-align: right; top: 138px; font-size: 38px; }
  .letterhead .contact { width: 757px; text-align: right; font-size: 12px; left: 0; }

  /* envelope */
  .envelope {
    position: absolute; left: 61px; top: 411px; width: 654px; height: 284px;
    background: var(--paper); border: 1.5px solid var(--ink);
  }
  .envelope .wordmark { left: 38px; top: 28px; font-size: 23px; }
  .envelope .contact { left: 38px; font-size: 7px; }
  .envelope .seal {
    position: absolute; right: 26px; bottom: 22px; width: 22px; height: 22px;
    border-radius: 50%; background: var(--leaf);
  }

  /* business card */
  .business-card {
    position: absolute; left: 59px; top: 819px; width: 336px; height: 188px;
    background: var(--paper); border: 1.5px solid var(--ink);
    transform: rotate(-3.3deg);
  }
  .card-name {
    position: absolute; right: 16px; top: 4px;
    font-family: "Mulish", sans-serif; font-weight: 800; font-size: 21px; line-height: 1; white-space: nowrap;
  }
  .card-title {
    position: absolute; right: 16px; top: 31px;
    font-family: "Mulish", sans-serif; font-weight: 800; font-size: 9px; line-height: 1;
  }
  .card-details { right: 16px; top: 44px; text-align: right; font-size: 9.5px; }
  .business-card .wordmark { right: 8px; top: 112px; font-size: 33px; }

  /* presentation note */
  .presented-for { text-align: right; padding: 16px 18px 0 0; }
  .presented-for .lead {
    font-family: "Mulish", sans-serif; font-weight: 800; font-size: 46px; line-height: 1; color: #000;
  }
  .presented-for .client {
    font-family: "Mulish", sans-serif; font-weight: 800; font-size: 26px; line-height: 1.3; color: #000;
  }
</style>
</head>
<body>
  <div class="backdrop" role="img" aria-label="Soft grey geometric triangle pattern background"></div>

  <h2 class="section-label" style="left:47px; top:48px;">letterhead</h2>
  <section class="panel" style="left:23px; top:73px; width:826px; height:255px;"></section>
  <div class="letterhead">
    <svg width="900" height="330" style="position:absolute; left:0; top:0;" aria-hidden="true">
      <polygon fill="#ffffff" stroke="#111" stroke-width="1.5"
        points="58,93 797,93 797,302 725,282 652,309 578,282 505,309 430,282 357,309 282,282 210,309 133,282 58,302"/>
    </svg>
    <div class="band" style="left:373px; top:172px; width:425px; height:12px;"></div>
    <div class="wordmark">Fernway Grounds</div>
    <div class="contact" style="top:191px;">Address Line<span class="sep"></span>City, State Zip</div>
    <div class="contact" style="top:205px;">Phone Number<span class="sep"></span>Website</div>
  </div>

  <h2 class="section-label" style="left:47px; top:355px;">envelope</h2>
  <section class="panel" style="left:23px; top:380px; width:732px; height:340px;"></section>
  <div class="envelope">
    <div class="wordmark">Fernway Grounds</div>
    <div class="band" style="left:0; top:47px; width:214px; height:7px;"></div>
    <div class="contact" style="top:57px;">Address Line 1<span class="sep"></span>City, State Zip</div>
    <div class="contact" style="top:66px;">Phone Number<span class="sep"></span>Website</div>
    <div class="seal"></div>
  </div>

  <h2 class="section-label" style="left:55px; top:748px;">business card</h2>
  <section class="panel" style="left:30px; top:773px; width:405px; height:264px;"></section>
  <div class="business-card">
    <div class="card-name">First Last</div>
    <div class="band" style="left:222px; top:28px; width:114px; height:4px;"></div>
    <div class="card-title">Title</div>
    <div class="contact card-details">Phone Number<br>Email Address<br>Address Line 1<br>City, State Zip</div>
    <div class="wordmark">Fernway Grounds</div>
    <div class="band" style="left:11px; top:140px; width:325px; height:9px;"></div>
  </div>

  <section class="panel presented-for" style="left:460px; top:1029px; width:425px; height:135px;">
    <p class="lead">designed for:</p>
    <p class="client">fernway grounds</p>
  </section>

</body>
</html>
```